■依頼の目的/概要
電子書籍の表紙デザインをお願いします。

経営者のための「黄金オフィス気学」
〜歴史に名を遺す名将や成功者はみんなやっていた〜

著者
経営者専属:開運鑑定士 夕凪みのり

★読者限定プレゼント→今すぐあなたや社員の吉方位が分かる「本命掛早見表と八宅盤」

■本の内容
経営者向けの経営サポート本として「ビジネス風水」を具体的にご紹介しています。
「まえがき、目次、本文、後書き」原稿をファイル添付していますので、まえがきや目次等見ていただき、内容の雰囲気をご確認いただけると嬉しいです。

筆者(私)はタロット歴20年の電話占い師(夕凪みのり)です。本書の著者の肩書きは↑にも書いておりますように「経営者専属:開運鑑定士 夕凪みのり」でお願い致します。

■デザイン要望
経営者に魅力を感じていただきやすくパッと目を引き、どのような本なのかが一目で分かりやすいデザインが望ましいです。基本全部おまかせです。是非デザイナーさんの魅力と才能を発揮していただけたらと思います。

その他何かご不明な点がございましたら、お気軽にご質問下さい。
よろしくお願いいたします。
【画像サイズ】※RLQより抜粋(電子書籍はLumoraです)
表紙ファイルの理想的な寸法は、2,560✖️1,600ピクセルです。
注:画像の寸法は、1,000✖️625ピクセル以上であることが必要です。
画像の最大の寸法は、10,000✖️10,000ピクセルです。

Zentaro(Lumora)に表示された際はかなり小さくなる事を踏まえ、他の経営者向けの本と並んだ時、目が止まりやすい一冊になるか?という点を意識し、選ばさせて頂きました。

表紙デザインの色や見た目のインパクトと文字の分かりやすさ、サブタイトルまでしっかりアピールされている所が気に入りました。

クラフターの皆様、この度はコンペにご参加いただきまして誠にありがとうございました。
本当に素晴らしいデザインばかりで、正直選考はとても難航いたしました。

今回は沢山のご提案の中から1つを選ぶことがとても難しかった為「他の経営者向けの本と並んだ時、目が止まりやすい一冊になるか?内容が分かりやすいか?」を軸に、著者仲間30名にアンケートを実施し当選作品を決定させて頂きました。

改めまして、皆様の才能を発揮して頂き素晴らしい作品をご提案頂きました事、心より感謝申し上げます。誠にありがとうございました。

```html
<!DOCTYPE html>
<html lang="ja">
<head>
<meta charset="utf-8">
<title>経営者のためのビジネス風水</title>
<link href="https://fonts.googleapis.com/css2?family=Dela+Gothic+One&family=Noto+Sans+JP:wght@700;900&family=Noto+Serif+JP:wght@700;900&display=swap" rel="stylesheet">
<style>
  :root {
    --compass-deep: #1f4fa8;
    --compass-mid: #3f7fd0;
    --compass-light: #9cc6ee;
    --bagua-red: #c8202a;
    --title-yellow: #ffe600;
    --title-red: #e3141b;
    --ink: #111111;
    --paper: #ffffff;
    --gift-yellow: #fff200;
  }
  html, body { margin: 0; padding: 0; overflow: hidden; }
  body { width: 750px; height: 1200px; background: #ffffff; }
  .cover {
    position: relative;
    width: 750px; height: 1200px;
    overflow: hidden;
    font-family: "Noto Sans JP", sans-serif;
  }
  .compass-art {
    position: absolute; inset: 0;
    background:
      radial-gradient(circle at 110px 930px, var(--bagua-red) 0 150px, rgba(200,32,42,0) 260px),
      radial-gradient(circle at 520px 420px, var(--compass-light) 0, var(--compass-mid) 45%, var(--compass-deep) 100%);
  }
  .lower-panel { position: absolute; left: 0; top: 690px; width: 750px; height: 510px; }
  .vertical { position: absolute; writing-mode: vertical-rl; margin: 0; white-space: nowrap; }
  .author-role {
    left: 30px; top: 26px;
    font: 700 22px/1 "Noto Sans JP", sans-serif;
    color: var(--ink); letter-spacing: 2px;
  }
  .author-name {
    left: 64px; top: 24px;
    font: 900 54px/1 "Noto Serif JP", serif;
    color: var(--ink); letter-spacing: 6px;
  }
  .title-lead {
    left: 408px; top: 90px;
    font: 900 46px/1 "Noto Sans JP", sans-serif;
    color: var(--ink); letter-spacing: -1px;
    -webkit-text-stroke: 8px #ffffff; paint-order: stroke fill;
  }
  .title-main {
    left: 466px; top: 60px;
    font: 400 190px/1 "Dela Gothic One", sans-serif;
    color: var(--title-yellow); letter-spacing: -40px;
    -webkit-text-stroke: 16px var(--title-red); paint-order: stroke fill;
    text-shadow: 6px 6px 0 rgba(0,0,0,.35);
  }
  .title-sub {
    left: 168px; top: 96px;
    font: 400 140px/1 "Dela Gothic One", sans-serif;
    color: var(--title-red); letter-spacing: 0;
    -webkit-text-stroke: 14px var(--title-yellow); paint-order: stroke fill;
    text-shadow: 5px 5px 0 rgba(0,0,0,.35);
  }
  .catchcopy {
    position: absolute; left: 128px; top: 805px; margin: 0;
    font: 900 50px/110px "Noto Serif JP", serif;
    color: var(--ink); letter-spacing: -2px; white-space: nowrap;
    transform: rotate(-3deg); transform-origin: left top;
  }
  .gift {
    position: absolute; left: 500px; top: 918px; width: 235px;
    font: 700 22px/1.35 "Noto Sans JP", sans-serif; color: var(--ink);
    white-space: nowrap; letter-spacing: -0.5px;
  }
  .gift-label { color: var(--title-red); font-weight: 900; margin: 0 0 2px; font-size: 22px; }
  .gift-text { margin: 0; }
  .gift-key { font-size: 26px; font-weight: 900; }
  .gift-item {
    display: inline-block; margin-top: 6px; padding: 4px 8px;
    background: var(--gift-yellow); color: var(--title-red);
    font-weight: 900; font-size: 25px; line-height: 1.3;
  }
</style>
</head>
<body>
<main class="cover">
  <div class="compass-art" role="img" aria-label="青い風水羅盤と赤い八卦盤のイラスト"></div>
  <svg class="lower-panel" viewBox="0 0 750 510" aria-hidden="true">
    <path d="M0 80 C120 40 220 10 340 20 C470 30 600 10 750 0 L750 510 L0 510 Z" fill="var(--paper)"/>
  </svg>

  <p class="vertical author-role">経営者専属 開運鑑定士</p>
  <p class="vertical author-name">夕凪みのり</p>

  <h1>
    <span class="vertical title-lead">経営者のための</span>
    <span class="vertical title-main">ビジネス</span>
    <span class="vertical title-sub">風水</span>
  </h1>

  <p class="catchcopy">歴史に名を遺す名将や<br>成功者はみんな<br>やっていた!!</p>

  <div class="gift">
    <p class="gift-label">読者限定プレゼント</p>
    <p class="gift-text">今すぐあなたや社員の<br><span class="gift-key">吉方位</span>が分かる</p>
    <span class="gift-item">「本命掛早見表<br>と八宅盤」</span>
  </div>
</main>
</body>
</html>
```